I am a company selling interior designing materials

HI, I am selling interior design materials and require a namecard which is more outstanding while following a certain details placement as attached.

My clients are mainly interior designers so it has to attract their attention rather than feeling that its "just another namecard". I am selling wallcoverings, fabrics, acoustics and carpets.

Target Market(s)

interior designers designing hotels, commerical offices.

Contact Information for Business Card

As per attached.
Please change address to 47 Jalan 16 Tampines #05-02 Velmora Building Singapore 527314

Font styles to use
Other font styles liked:
• calibri

Requirements
Must have
• (1) company logo on top in the middle. Placement of contac details to be the same
• (2) company color is blue/green cymk 75/8/42/0
• (3) "KTV" logo to be prominent
• (4) You may change the logo but there should be a "swirl" surrounding the word KTV like current logo. The swirl pattern does not need to follow current logo and you may propose.
Should not have
• (1) there should not be any designs above "KTV" logo
• (2) no sharp triangles or angles

```html
<!DOCTYPE html>
<html lang="en">
<head>
<meta charset="utf-8">
<title>KTV Name Card</title>
<link rel="stylesheet" href="https://fonts.googleapis.com/css2?family=Open+Sans:ital,wght@0,400;0,600;0,700;0,800;1,400&display=swap">
<style>
  :root {
    --stage: #262626;
    --teal: #3cb8aa;
    --teal-dark: #2fa698;
    --slate: #6b6b6b;
    --slate-light: #7c7c7c;
    --slate-dark: #5a5a5a;
    --white: #ffffff;
    --silver: #8a8a8a;
    --accent-red: #e8393f;
  }
  * { margin: 0; padding: 0; box-sizing: border-box; }
  html, body { width: 1200px; height: 960px; overflow: hidden; background: var(--stage); }
  body { font-family: "Open Sans", sans-serif; position: relative; }

  .card {
    position: absolute;
    left: 250px;
    width: 700px;
    height: 400px;
    border-radius: 4px;
    overflow: hidden;
    box-shadow: 0 14px 30px rgba(0,0,0,.45);
  }

  /* Front */
  .card-front { top: 40px; background: linear-gradient(135deg, var(--teal-dark), var(--teal) 60%, #5cc6ba); }
  .front-brand {
    position: absolute; left: 0; right: 0; top: 120px;
    text-align: center;
  }
  .front-brand .wordmark {
    font-weight: 800; font-size: 110px; letter-spacing: 4px; color: var(--silver); line-height: 1;
  }
  .front-brand .dot {
    display: inline-block; width: 18px; height: 18px; border-radius: 50%;
    background: var(--silver); margin-left: 10px; vertical-align: 14px;
  }
  .front-tagline {
    position: absolute; left: 0; right: 0; top: 258px;
    text-align: center; font-size: 15px; letter-spacing: 1.2px; color: var(--white);
  }

  /* Back */
  .card-back { top: 500px; background: linear-gradient(160deg, var(--slate-dark), var(--slate) 45%, var(--slate-light)); }
  .back-stripes { position: absolute; inset: 0; }
  .back-company {
    position: absolute; left: 40px; top: 34px;
    font-style: italic; font-size: 14px; color: var(--white);
  }
  .back-brand {
    position: absolute; left: 40px; top: 70px; width: 300px; text-align: center;
    font-weight: 800; font-size: 64px; letter-spacing: 2px; color: var(--white); line-height: 1;
  }
  .name-band {
    position: absolute; left: 390px; right: 0; top: 118px; height: 44px;
    background: var(--teal); border-radius: 3px 0 0 3px;
    display: flex; align-items: center; justify-content: flex-end; padding-right: 40px;
  }
  .name-band .name { font-size: 26px; color: var(--white); letter-spacing: 1px; }
  .name-band .first { font-weight: 700; }
  .name-band .last { font-weight: 400; }

  .contacts { position: absolute; right: 44px; top: 186px; width: 480px; text-align: right; color: var(--white); }
  .contact { position: relative; margin-bottom: 20px; font-size: 16px; letter-spacing: .8px; line-height: 1.35; }
  .contact .icon { display: block; margin-left: auto; width: 18px; height: 16px; margin-bottom: 2px; }
  .contact .rule { display: block; margin-left: auto; width: 40px; height: 2px; background: var(--teal); margin-bottom: 4px; }
</style>
</head>
<body>

<section class="card card-front">
  <div class="front-brand"><span class="wordmark">KTV</span><span class="dot"></span></div>
  <p class="front-tagline">Kestavin Textile Ventures Pte Ltd</p>
</section>

<section class="card card-back">
  <svg class="back-stripes" width="700" height="400" viewBox="0 0 700 400">
    <polygon points="150,400 250,400 560,0 470,0" fill="#747474"/>
    <line x1="150" y1="400" x2="470" y2="0" stroke="#555" stroke-width="2"/>
    <line x1="250" y1="400" x2="560" y2="0" stroke="#555" stroke-width="2"/>
  </svg>

  <p class="back-company">Kestavin Textile Ventures Pte Ltd</p>
  <div class="back-brand">KTV</div>

  <div class="name-band"><span class="name"><span class="first">LINA</span> <span class="last">TAN</span></span></div>

  <div class="contacts">
    <div class="contact">
      <svg class="icon" viewBox="0 0 18 16"><path d="M2 6c0-2 3-4 7-4s7 2 7 4v1h-3V5H5v2H2z M4 8h10l2 6H2z" fill="var(--accent-red)"/></svg>
      <span class="rule"></span>
      (65) 8172 4053
    </div>
    <div class="contact">
      <svg class="icon" viewBox="0 0 18 16"><rect x="1.5" y="3" width="15" height="10" rx="1" fill="none" stroke="var(--accent-red)" stroke-width="1.5"/><path d="M2 4l7 5 7-5" fill="none" stroke="var(--accent-red)" stroke-width="1.5"/></svg>
      <span class="rule"></span>
      lina@ktvfurnishings.com
    </div>
    <div class="contact">
      <svg class="icon" viewBox="0 0 18 20" style="height:20px"><path d="M9 1a6 6 0 0 1 6 6c0 5-6 12-6 12S3 12 3 7a6 6 0 0 1 6-6z" fill="var(--accent-red)"/><circle cx="9" cy="7" r="2.2" fill="var(--slate)"/></svg>
      <span class="rule"></span>
      47 Jalan 16 Tampines #05-02 Velmora Building<br>Singapore 527314
    </div>
  </div>
</section>

</body>
</html>
```